I need the following on my business card:
- Name: Dana Whitcomb
- License # 0M93216
- Title: Producer
- Phone: (555) 017-3904
- Email: Dana@CorbelInsuranceServices.com

- Company: Corbel Insurance Services
- Address: 27408 Larkmoor Ave Suite 610, Sherman Oaks, CA 90217
- Website: www.CorbelInsuranceServices.com

Also add our slogan on the card: "Where Trust Meets Coverage"

```html
<!DOCTYPE html>
<html lang="en">
<head>
<meta charset="utf-8">
<title>Corbel Insurance Services – Business Card</title>
<link href="https://fonts.googleapis.com/css2?family=Outfit:wght@400;500;600;700&display=swap" rel="stylesheet">
<style>
  :root {
    --navy: #002c7a;
    --green: #0a9a3a;
    --ink: #333333;
    --paper: #ffffff;
    --backdrop: #b3b3b3;
  }
  * { margin: 0; padding: 0; box-sizing: border-box; }
  html, body {
    width: 1093px; height: 1200px; overflow: hidden;
    background: var(--backdrop);
    font-family: "Outfit", sans-serif;
  }
  .card {
    position: absolute;
    left: 265px;
    width: 578px;
    height: 356px;
    border-radius: 26px;
    overflow: hidden;
  }
  .card--front { top: 226px; background: var(--paper); }
  .card--back { top: 621px; background: var(--navy); }

  .edge-band { position: absolute; left: 0; width: 13px; }
  .edge-band--green { top: 0; height: 95px; background: var(--green); }
  .edge-band--navy { top: 101px; bottom: 0; background: var(--navy); }

  .identity { position: absolute; left: 43px; top: 56px; }
  .identity__name {
    color: var(--navy); font-weight: 700; font-size: 24px;
    line-height: 1; letter-spacing: -0.3px; text-transform: uppercase;
  }
  .identity__title { color: var(--green); font-size: 15.5px; font-weight: 500; margin-top: 3px; }

  .brand-mark {
    position: absolute; right: 20px; top: 40px;
    display: flex; align-items: center; gap: 10px;
  }
  .brand-mark__dot { width: 14px; height: 14px; background: var(--green); flex: none; }
  .brand-mark__name {
    color: var(--navy); font-weight: 700; font-size: 18px; line-height: 24px;
    letter-spacing: 0.6px; text-transform: uppercase; text-align: right;
  }
  .brand-mark__name span { display: block; }

  .office { position: absolute; left: 32px; top: 175px; color: var(--ink); }
  .office__company {
    color: var(--navy); font-weight: 600; font-size: 13.5px;
    text-transform: uppercase; letter-spacing: -0.1px; margin-bottom: 4px;
  }
  .office__line { font-size: 15.5px; line-height: 22px; }

  .contacts { position: absolute; left: 32px; top: 258px; list-style: none; color: var(--ink); }
  .contacts li { display: flex; align-items: center; gap: 8px; font-size: 15.5px; line-height: 21.5px; }
  .contacts svg { width: 15px; height: 15px; flex: none; }

  .license { position: absolute; right: 27px; top: 302px; font-size: 15.5px; color: var(--green); }
  .license__number { color: var(--navy); }

  .back-brand {
    position: absolute; left: 0; right: 0; top: 170px;
    text-align: center; color: var(--green);
    font-weight: 600; font-size: 22px; letter-spacing: 3px; text-transform: uppercase;
  }
  .slogan {
    position: absolute; left: 0; right: 0; top: 258px;
    text-align: center; color: var(--paper);
    font-weight: 600; font-size: 19.5px; letter-spacing: -0.3px; text-transform: uppercase;
  }
</style>
</head>
<body>
  <section class="card card--front">
    <div class="edge-band edge-band--green"></div>
    <div class="edge-band edge-band--navy"></div>

    <div class="identity">
      <h1 class="identity__name">Dana Whitcomb</h1>
      <p class="identity__title">Producer</p>
    </div>

    <div class="brand-mark">
      <span class="brand-mark__dot"></span>
      <p class="brand-mark__name"><span>Corbel</span><span>Insurance Services</span></p>
    </div>

    <div class="office">
      <p class="office__company">Corbel Insurance Services</p>
      <p class="office__line">27408 Larkmoor Ave Suite 610</p>
      <p class="office__line">Sherman Oaks, CA 90217</p>
    </div>

    <ul class="contacts">
      <li>
        <svg viewBox="0 0 24 24" fill="none" stroke="var(--green)" stroke-width="2.4" stroke-linecap="round" stroke-linejoin="round"><path d="M5 3h4l2 5-2.5 1.5a11 11 0 0 0 6 6L16 13l5 2v4a2 2 0 0 1-2 2A16 16 0 0 1 3 5a2 2 0 0 1 2-2z"/></svg>
        (555) 017-3904
      </li>
      <li>
        <svg viewBox="0 0 24 24"><rect x="1" y="5" width="22" height="14" fill="var(--green)"/><path d="M1 5l11 8 11-8" fill="none" stroke="#fff" stroke-width="1.6"/></svg>
        Dana@CorbelInsuranceServices.com
      </li>
      <li>
        <svg viewBox="0 0 24 24" fill="none" stroke="var(--green)" stroke-width="1.8"><circle cx="12" cy="12" r="10"/><ellipse cx="12" cy="12" rx="4.5" ry="10"/><path d="M2 12h20M4 7h16M4 17h16"/></svg>
        www.CorbelInsuranceServices.com
      </li>
    </ul>

    <p class="license">License # <span class="license__number">0M93216</span></p>
  </section>

  <section class="card card--back">
    <p class="back-brand">Corbel Insurance Services</p>
    <p class="slogan">Where Trust Meets Coverage</p>
  </section>
</body>
</html>
```